Need a website to promote and sell my book

Using images from the book, I need a website designed that helps promote the book and eventually sell it.
*Need a landing page
*About the author page
*Storefront page to purchase
*Coming soon page
*"Featured in" page that can link to news articles etc.
The images posted here are examples, the winner of the contest will get the images from the finished book. I will provide the exact text to the winner of the contest.

I can also provide images of kids reading the book. For now, I'll just use one, the winner can have them all to choose from.
Updates

Extending deadline to allow for a few more designers to submit and to allow time for me to review and hold a poll

Target Market(s)

Parents, aunts, uncles, grandparents, friends who have kids; teachers, daycare teachers, babysitters etc.

Industry/Entity Type

Custom Publishing

Coding

Coded - Design and coding required

Number of Pages Required

5+ page

Font styles to use
Sans Serif

Colors

Designer to choose colors to be used in the design.

Requirements
Must have
• It must have a fun feel like the book.
Nice to have
• Would be great to have a section that automatically pulls tweets about the book into it.

```html
<!DOCTYPE html>
<html lang="en">
<head>
<meta charset="utf-8">
<title>Bubbles &amp; Beakers</title>
<link href="https://fonts.googleapis.com/css2?family=Montserrat:wght@400;500;600;700&display=swap" rel="stylesheet">
<style>
:root{
  --teal:#1aa5ad;
  --teal-bright:#26c6d1;
  --teal-deep:#12909a;
  --mint:#e9f9fb;
  --mint-soft:#f3fcfd;
  --ink:#151a1f;
  --grey:#7d8890;
  --white:#ffffff;
  --faint:#e2f5f8;
}
*{margin:0;padding:0;box-sizing:border-box}
html,body{width:1200px;height:4307px;overflow:hidden;background:var(--white)}
body{font-family:"Montserrat",sans-serif;color:var(--ink)}
.page{position:relative;width:1200px;height:4307px;overflow:hidden;background:var(--white)}
.abs{position:absolute}
.shapes{position:absolute;left:0;top:0;width:1200px;height:4307px}
.brand{display:flex;align-items:center;gap:14px;font-weight:600;font-size:24px;line-height:1.25;color:var(--ink)}
.brand-dot{width:34px;height:34px;border-radius:50%;border:3px solid var(--teal);flex:none}
.btn{position:absolute;display:flex;align-items:center;justify-content:center;gap:8px;background:var(--teal);color:var(--white);font-weight:600;font-size:14px;border-radius:4px 18px 4px 18px}
.btn.outline{background:var(--white);color:var(--teal);font-size:18px;border-radius:6px 26px 6px 26px}
.arrow{width:14px;height:8px}
.menu{position:absolute;left:1002px;top:50px;width:38px}
.menu span{display:block;height:4px;background:var(--teal);border-radius:2px;margin-bottom:6px;margin-left:auto}
.ghost{position:absolute;font-weight:700;color:var(--faint);letter-spacing:2px;white-space:nowrap}
h1,h2{position:absolute;font-weight:600;color:var(--ink)}
.hero-title{left:162px;top:205px;font-size:36px;line-height:1.5;width:680px;white-space:nowrap}
.hero-text{left:162px;top:330px;width:490px;font-size:12px;line-height:1.75;color:var(--ink)}
.section-title{font-size:36px}
.center-title{left:0;width:1200px;text-align:center;font-size:36px}
.copy{position:absolute;font-size:11.5px;line-height:1.75;color:var(--grey)}
.art{position:absolute}
.dots{position:absolute;left:540px;top:620px;display:flex;gap:40px;align-items:center}
.dots i{width:9px;height:9px;border-radius:50%;background:#b9e6ea;display:block}
.dots i.on{width:20px;height:20px;border:3px solid #b9e6ea;background:var(--white)}
.play{position:absolute;left:920px;top:1613px;width:44px;height:44px;border-radius:50%;border:3px solid var(--white)}
.play:after{content:"";position:absolute;left:15px;top:10px;border-left:14px solid var(--white);border-top:9px solid transparent;border-bottom:9px solid transparent}
.store-card{position:absolute;left:485px;top:1994px;width:474px;height:246px;background:var(--white);border-radius:6px;box-shadow:0 8px 30px rgba(20,80,90,.08);overflow:hidden}
.store-card .swash{position:absolute;right:-40px;bottom:-60px;width:260px;height:140px;border-radius:50%;background:var(--mint)}
.store-card h3{position:absolute;left:30px;top:30px;font-size:20px;font-weight:600}
.store-card .by{position:absolute;left:30px;top:62px;font-size:11px;color:var(--teal)}
.store-card .copy{left:30px;top:84px;width:425px;color:var(--grey)}
.feature{position:absolute;width:220px;height:234px;background:var(--white);border-radius:6px;box-shadow:0 6px 24px rgba(20,80,90,.1);text-align:center;padding-top:22px}
.feature svg{width:54px;height:54px}
.feature h4{font-size:13.5px;font-weight:600;margin:14px 0 12px}
.feature p{font-size:10.5px;line-height:1.85;color:var(--grey);padding:0 14px}
.feature a{display:block;margin-top:8px;font-size:11px;font-weight:600;color:var(--teal);text-decoration:none}
.news{position:absolute;top:3245px;width:276px;height:335px;background:var(--white);box-shadow:0 6px 24px rgba(20,80,90,.08)}
.news .thumb{position:absolute;left:8px;top:8px;width:260px;height:165px}
.news h5{position:absolute;left:12px;top:184px;width:255px;font-size:12px;font-weight:600;line-height:1.65}
.news .date{position:absolute;left:12px;top:226px;font-size:10.5px;color:var(--teal)}
.news p{position:absolute;left:12px;top:246px;width:255px;font-size:10.5px;line-height:1.85;color:var(--grey)}
.footer-nav{position:absolute;left:0;top:4125px;width:1200px;display:flex;justify-content:center;gap:40px;font-size:11px;color:var(--grey)}
.social{position:absolute;top:4178px;width:36px;height:36px;border-radius:50%;border:2px solid var(--teal)}
.legal{position:absolute;left:0;top:4258px;width:1200px;height:49px;background:var(--teal);color:var(--white);font-size:10.5px;display:flex;align-items:center;justify-content:center}
</style>
</head>
<body>
<div class="page">

<svg class="shapes" viewBox="0 0 1200 4307" aria-hidden="true">
  <path d="M0 380 C200 420 300 640 520 600 C700 570 800 460 1000 520 C1100 550 1160 600 1200 620 L1200 760 L0 760 Z" fill="var(--mint)"/>
  <path d="M152 175 C230 130 380 170 400 260 C420 360 320 420 300 520 C280 600 200 630 165 560 C140 500 210 440 180 360 C150 280 100 210 152 175 Z" fill="var(--teal)"/>
  <path d="M700 690 C720 600 800 560 880 600 L1200 560 L1200 700 C1100 740 960 720 700 690 Z" fill="var(--teal-bright)"/>
  <path d="M0 700 C300 760 520 720 760 760 C960 790 1100 760 1200 740 L1200 1330 C900 1390 500 1300 0 1380 Z" fill="var(--mint-soft)"/>
  <path d="M80 980 C140 920 230 930 250 990 C270 1060 180 1100 110 1080 C60 1060 50 1010 80 980 Z" fill="#fff3d6"/>
  <path d="M0 1420 C300 1380 600 1440 780 1480 C700 1560 560 1600 500 1520 C460 1470 520 1420 600 1460 Z" fill="var(--teal-bright)" opacity=".85"/>
  <path d="M0 1430 C400 1380 700 1450 900 1520 L1200 1560 L1200 1900 C1000 1920 800 1860 600 1760 C400 1660 200 1760 0 1700 Z" fill="var(--mint-soft)"/>
  <path d="M0 2420 C60 2440 100 2520 140 2560 C200 2620 300 2600 320 2640 C280 2700 170 2660 100 2620 C50 2590 20 2560 0 2560 Z" fill="var(--teal)"/>
  <path d="M1010 2620 C1050 2590 1060 2660 1040 2740 C1020 2830 980 2880 940 2880 C960 2800 980 2700 1010 2620 Z" fill="var(--teal-bright)"/>
  <path d="M0 2700 C300 2650 500 2700 700 2760 C900 2820 1100 2780 1200 2760 L1200 3100 L0 3100 Z" fill="var(--mint-soft)"/>
  <path d="M0 3150 C60 3180 90 3260 80 3320 L0 3340 Z" fill="var(--teal)"/>
  <path d="M270 3230 C285 3180 300 3160 310 3140 C320 3170 330 3210 335 3240 Z" fill="var(--teal)"/>
  <path d="M0 3380 C100 3500 80 3560 0 3600 Z" fill="var(--teal-bright)"/>
  <path d="M1130 3260 C1180 3280 1200 3300 1200 3320 L1200 3600 C1140 3560 1100 3460 1130 3260 Z" fill="var(--teal)"/>
  <path d="M0 3590 C260 3560 500 3620 720 3640 C900 3660 1080 3620 1200 3600 L1200 4260 L0 4260 Z" fill="var(--mint)"/>
  <path d="M720 3650 C820 3620 900 3680 1000 3700 C1080 3720 1150 3700 1200 3660 L1200 3800 C1100 3820 1000 3780 920 3800 C860 3820 800 3760 720 3650 Z" fill="var(--teal-bright)"/>
  <path d="M700 3700 C800 3740 900 3820 1040 3860 C1100 3880 1160 3870 1200 3850 L1200 3900 C1100 3920 960 3900 820 3840 C760 3800 720 3760 700 3700 Z" fill="var(--teal)"/>
  <path d="M0 3960 C100 4000 200 4080 300 4120 C220 4140 80 4100 0 4080 Z" fill="#c9eff3"/>
  <path d="M0 4150 C40 4170 50 4210 40 4240 L0 4250 Z" fill="var(--teal)"/>
</svg>

<!-- header -->
<div class="brand abs" style="left:160px;top:28px"><span class="brand-dot"></span><span>Bubbles &amp;<br>Beakers</span></div>
<div class="btn" style="left:826px;top:45px;width:134px;height:38px">Get In Touch</div>
<div class="menu"><span style="width:38px"></span><span style="width:30px"></span><span style="width:22px"></span></div>

<!-- hero -->
<div class="ghost" style="left:165px;top:165px;font-size:54px">CHEMISTRY</div>
<h1 class="hero-title">Chemistry is the study of<br>matter and all its aspects.</h1>
<p class="abs hero-text">Lorem Ipsum is simply dummy text of the printing and typesetting industry. Lorem Ipsum has been the industry's standard dummy text ever since the 1500s</p>
<div class="btn outline" style="left:162px;top:413px;width:218px;height:50px">Publish Your Book</div>
<div class="art" role="img" aria-label="Photo of a child writing at a desk" style="left:802px;top:385px;width:420px;height:330px;border-radius:180px 0 0 90px;background:linear-gradient(135deg,#5fb6b8,#2f8e93)"></div>
<div class="art" role="img" aria-label="Book cover badge with two cartoon children and title lettering" style="left:700px;top:125px;width:450px;height:345px;border-radius:48% 52% 46% 54%;background:linear-gradient(160deg,#f4559c,#e0317f);transform:rotate(-8deg)"></div>
<div class="dots"><i></i><i class="on"></i><i></i></div>

<!-- authors -->
<div class="art" role="img" aria-label="Small round book badge with a cartoon girl" style="left:178px;top:790px;width:118px;height:118px;border-radius:50%;background:linear-gradient(135deg,#3db9e6,#1c8fd0)"></div>
<div class="art" role="img" aria-label="Book illustration of children beside a toy box" style="left:117px;top:870px;width:421px;height:417px;border-radius:60% 40% 50% 50% / 40% 45% 55% 60%;background:linear-gradient(150deg,#9c9c82,#b8a86c 60%,#c3a35a)"></div>
<div class="ghost" style="left:613px;top:862px;font-size:56px">AUTHORS</div>
<h2 class="section-title" style="left:613px;top:897px">About Our Authors</h2>
<p class="copy" style="left:613px;top:960px;width:335px">Lorem Ipsum is simply dummy text of the printing and typesetting industry. Lorem Ipsum has been the industry's standard dummy text ever since the 1500s, when an unknown printer took a galley of type and scrambled it to make a type specimen book.</p>
<p class="copy" style="left:613px;top:1075px;width:335px">It has survived not only five centuries, but also the leap into electronic typesetting, remaining essentially unchanged.</p>
<div class="btn" style="left:612px;top:1150px;width:156px;height:40px">Read More <svg class="arrow" viewBox="0 0 14 8"><path d="M0 4h12M9 1l3 3-3 3" stroke="#fff" stroke-width="1.5" fill="none"/></svg></div>
<div class="art" role="img" aria-label="Tilted book badge with a cartoon girl" style="left:935px;top:1190px;width:170px;height:118px;border-radius:50%;background:linear-gradient(135deg,#8a4fc6,#5b2e9a);transform:rotate(18deg)"></div>

<!-- why chemistry -->
<div class="ghost" style="left:162px;top:1420px;font-size:60px">COMING SOON</div>
<h2 class="section-title" style="left:162px;top:1458px">Why Chemistry</h2>
<p class="copy" style="left:162px;top:1520px;width:335px">Lorem Ipsum is simply dummy text of the printing and typesetting industry. Lorem Ipsum has been the industry's standard dummy text ever since the 1500s, when an unknown printer took a galley of type and scrambled it to make a type specimen book.</p>
<p class="copy" style="left:162px;top:1635px;width:335px">It has survived not only five centuries, but also the leap into electronic typesetting, remaining essentially unchanged.</p>
<div class="btn" style="left:162px;top:1711px;width:156px;height:40px">Read More <svg class="arrow" viewBox="0 0 14 8"><path d="M0 4h12M9 1l3 3-3 3" stroke="#fff" stroke-width="1.5" fill="none"/></svg></div>
<div class="art" role="img" aria-label="Video still of children drawing at a classroom table" style="left:685px;top:1350px;width:540px;height:575px;border-radius:55% 0 0 45% / 50% 0 0 60%;background:linear-gradient(150deg,#6cc3c6,#2f9aa1 60%,#248a92)"></div>
<div class="play"></div>

<!-- store -->
<div class="art" role="img" aria-label="Small book cover badge" style="left:28px;top:1862px;width:138px;height:104px;border-radius:6px;background:linear-gradient(135deg,#f05a3b,#f7b234)"></div>
<div class="ghost" style="left:0;width:1200px;text-align:center;top:1825px;font-size:58px">STORE</div>
<h2 class="center-title" style="top:1858px">Our Store</h2>
<div class="store-card"><div class="swash"></div>
  <h3>Bubbles &amp; Beakers</h3>
  <div class="by">Written By: Dana Moreland, PhD</div>
  <p class="copy">Lorem Ipsum is simply dummy text of the printing and typesetting industry. Lorem Ipsum has been the industry's standard dummy text ever since the 1500s, when an unknown printer took a galley of type and scrambled it to make a type specimen book.</p>
</div>
<div class="btn" style="left:511px;top:2167px;width:122px;height:39px">Buy Now</div>
<div class="art" role="img" aria-label="Hardcover book with illustrated cover of children" style="left:225px;top:1947px;width:260px;height:338px;background:linear-gradient(160deg,#6fc7e9,#f4e3a8 70%,#f3c46a);box-shadow:0 18px 40px rgba(0,0,0,.18)"></div>

<!-- featured -->
<div class="art" role="img" aria-label="Cartoon boy with a ball in a round frame" style="left:1055px;top:2340px;width:100px;height:165px;border-radius:50%;background:linear-gradient(135deg,#f7a33b,#ea6c2a)"></div>
<div class="ghost" style="left:0;width:1200px;text-align:center;top:2375px;font-size:62px">FEATURED</div>
<h2 class="center-title" style="top:2408px">Our Featured</h2>

<div class="feature" style="left:485px;top:2507px">
  <svg viewBox="0 0 54 54" fill="none" stroke="var(--teal)" stroke-width="2"><rect x="8" y="10" width="38" height="34" rx="2"/><path d="M27 10v34M13 18h9M13 24h9M13 30h9M32 18h9M32 30l4-5 5 5"/></svg>
  <h4>Inspection &amp; Expriement</h4>
  <p>Lorem Ipsum is simply dummy text of the printing and typesetting industry. Lorem Ipsum has been the industry's standard dummy text.</p>
  <a>Read More &rarr;</a>
</div>
<div class="feature" style="left:246px;top:2657px">
  <svg viewBox="0 0 54 54" fill="none" stroke="var(--teal)" stroke-width="2"><path d="M20 8l10 6-8 14-10-6zM16 40h24M22 46h26M34 22c8 4 8 16 0 20"/></svg>
  <h4>Laboratory</h4>
  <p>Lorem Ipsum is simply dummy text of the printing and typesetting industry. Lorem Ipsum has been the industry's standard dummy text.</p>
  <a>Read More &rarr;</a>
</div>
<div class="feature" style="left:735px;top:2657px">
  <svg viewBox="0 0 54 54" fill="none" stroke="var(--teal)" stroke-width="2"><circle cx="27" cy="27" r="8"/><circle cx="27" cy="8" r="3"/><circle cx="27" cy="46" r="3"/><circle cx="10" cy="18" r="3"/><circle cx="44" cy="18" r="3"/><circle cx="10" cy="36" r="3"/><circle cx="44" cy="36" r="3"/><path d="M27 11v8M27 35v8M13 19l7 4M41 19l-7 4M13 35l7-4M41 35l-7-4"/></svg>
  <h4>Chemistry Sturcture</h4>
  <p>Lorem Ipsum is simply dummy text of the printing and typesetting industry. Lorem Ipsum has been the industry's standard dummy text.</p>
  <a>Read More &rarr;</a>
</div>
<div class="feature" style="left:485px;top:2761px">
  <svg viewBox="0 0 54 54" fill="none" stroke="var(--teal)" stroke-width="2"><path d="M18 8h14M22 8v14l-10 18a4 4 0 0 0 4 6h18a4 4 0 0 0 4-6L28 22V8M15 34h24M42 8v38"/></svg>
  <h4>Science Flask</h4>
  <p>Lorem Ipsum is simply dummy text of the printing and typesetting industry. Lorem Ipsum has been the industry's standard dummy text.</p>
  <a>Read More &rarr;</a>
</div>
<div class="art" role="img" aria-label="Oval book badge with two cartoon children" style="left:60px;top:2945px;width:125px;height:92px;border-radius:50%;background:linear-gradient(135deg,#f4559c,#e0317f);transform:rotate(-10deg)"></div>

<!-- news -->
<div class="ghost" style="left:0;width:1200px;text-align:center;top:3115px;font-size:62px">INSIGHTS</div>
<h2 class="center-title" style="top:3150px">Latest News</h2>

<div class="news" style="left:162px">
  <div class="thumb" role="img" aria-label="Book page illustration of children by a toy box" style="background:linear-gradient(150deg,#b9b38e,#a99a66)"></div>
  <h5>Lorem Ipsum is simply dummy text of the printing and typesetting industry.</h5>
  <div class="date">7 December 2019</div>
  <p>Lorem Ipsum is simply dummy text of the printing and typesetting industry. Lorem Ipsum has been the industry's standard dummy text ever since the 1500s.</p>
</div>
<div class="news" style="left:462px">
  <div class="thumb" role="img" aria-label="Book cover illustration with title lettering and children" style="background:linear-gradient(160deg,#3f8f76,#6aa088 60%,#5c8d72)"></div>
  <h5>Lorem Ipsum is simply dummy text of the printing and typesetting industry.</h5>
  <div class="date">7 December 2019</div>
  <p>Lorem Ipsum is simply dummy text of the printing and typesetting industry. Lorem Ipsum has been the industry's standard dummy text ever since the 1500s.</p>
</div>
<div class="news" style="left:762px">
  <div class="thumb" role="img" aria-label="Book page illustration of a classroom experiment" style="background:linear-gradient(150deg,#c9a56a,#8f7a5a)"></div>
  <h5>Lorem Ipsum is simply dummy text of the printing and typesetting industry.</h5>
  <div class="date">7 December 2019</div>
  <p>Lorem Ipsum is simply dummy text of the printing and typesetting industry. Lorem Ipsum has been the industry's standard dummy text ever since the 1500s.</p>
</div>
<div class="btn" style="left:521px;top:3633px;width:156px;height:40px">Explore More</div>

<!-- footer -->
<div class="art" role="img" aria-label="Oval illustration of children reading together" style="left:832px;top:3910px;width:329px;height:110px;border-radius:50%;background:linear-gradient(135deg,#6fc7e9,#f3c46a)"></div>
<div class="brand abs" style="left:476px;top:4020px"><span class="brand-dot"></span><span>Bubbles &amp;<br>Beakers</span></div>
<nav class="footer-nav"><span>Home</span><span>About Us</span><span>Store</span><span>Features</span><span>News</span><span>Contact Us</span></nav>
<div class="social" style="left:500px" aria-label="Social profile"></div>
<div class="social" style="left:552px" aria-label="Social profile"></div>
<div class="social" style="left:604px" aria-label="Social profile"></div>
<div class="social" style="left:657px" aria-label="Social profile"></div>
<div class="legal">Copyright &copy; 2019 Bubbles &amp; Beakers Terms &amp; Conditions | Privacy Policy.</div>

</div>
</body>
</html>
```